verdant harbour requires some business cards

I need some business cards created that feature the company's newly designed logo. The business cards need to be be double sided and be a standard Australian size of 90mm x 55mm

Target Market(s)

business professionals, company executives, local goverment

Industry/Entity Type

Business

Requirements
Must have
• Company's logo
• The information section must include
• Individual name:
• Position:
• Phone:
• Address:
• Email:
• Website: www.verdantharbour.example
• The cards need to be easily formatted so I can enter staff members details positions etc...
• I plan to get these printed at deskmarket so can you please ensure that all designs meet their printing requirements http://www.deskmarket.example/retail/b2c/opsProductCreate.do?qty=1&cardQty=1000&sided=double&productname=colourbusinesscards&category=businesscards
Nice to have
• I might like to see some of the services we offer printed on one of the faces:
• Lighting Design (architectural, commercial, residential, theatrical ,exterior, interior) Lighting Consultancy, Theatrical Consultancy

```html
<!DOCTYPE html>
<html lang="en">
<head>
<meta charset="utf-8">
<title>verdant harbour — business cards</title>
<link rel="stylesheet" href="https://fonts.googleapis.com/css2?family=Questrial&family=PT+Sans:wght@400;700&display=swap">
<style>
  :root {
    --backdrop: #d6d3cf;
    --card-dark: #1c1c1c;
    --card-light: #f4f4f4;
    --card-light-edge: #d9d9d9;
    --brand-blue: #2a9fd8;
    --name-navy: #1f2a5c;
    --ink: #222222;
  }
  * { box-sizing: border-box; margin: 0; padding: 0; }
  html, body {
    width: 960px;
    height: 1200px;
    overflow: hidden;
    background: var(--backdrop);
  }
  .canvas {
    position: relative;
    width: 960px;
    height: 1200px;
  }
  .card { position: absolute; overflow: hidden; }
  .card--back {
    left: 16px; top: 29px; width: 462px; height: 531px;
    background: var(--card-dark);
  }
  .card--info {
    left: 478px; top: 29px; width: 462px; height: 531px;
    background: radial-gradient(ellipse at 95% 45%, #ffffff 0%, var(--card-light) 35%, var(--card-light-edge) 100%);
  }
  .card--front {
    left: 10px; top: 590px; width: 928px; height: 536px;
    background: radial-gradient(ellipse at 50% 40%, #ffffff 0%, var(--card-light) 40%, var(--card-light-edge) 100%);
  }
  .brand {
    position: absolute;
    display: flex;
    align-items: center;
    font-family: "Questrial", "Century Gothic", sans-serif;
    color: var(--brand-blue);
    white-space: nowrap;
  }
  .brand__dot {
    display: inline-block;
    border-radius: 50%;
    background: var(--brand-blue);
  }
  .card--back .brand { left: 70px; top: 238px; font-size: 33px; gap: 14px; }
  .card--back .brand__dot { width: 22px; height: 22px; }
  .card--front .brand { left: 212px; top: 236px; font-size: 58px; gap: 22px; }
  .card--front .brand__dot { width: 38px; height: 38px; }

  .person {
    position: absolute;
    left: 262px; top: 38px;
    font-family: "PT Sans", "Myriad Pro", sans-serif;
  }
  .person__name { font-size: 29px; font-weight: 700; color: var(--name-navy); line-height: 1.1; }
  .person__role { font-size: 17px; color: var(--ink); padding-left: 6px; }

  .contact {
    position: absolute;
    left: 16px; top: 352px;
    font-family: "PT Sans", "Myriad Pro", sans-serif;
    font-size: 16px;
    color: var(--ink);
    line-height: 1.3;
  }
  .contact__row { margin-bottom: 10px; }
  .contact__row:last-child { margin-bottom: 0; }
  .contact__label { font-weight: 700; font-size: 21px; margin-right: 4px; }
  .contact__indent { padding-left: 4px; }
</style>
</head>
<body>
<main class="canvas">
  <section class="card card--back" aria-label="Card back">
    <div class="brand"><span class="brand__dot"></span><span class="brand__name">verdant harbour</span></div>
  </section>

  <section class="card card--info" aria-label="Card details side">
    <div class="person">
      <p class="person__name">John Doe</p>
      <p class="person__role">Manager</p>
    </div>
    <div class="contact">
      <p class="contact__row"><span class="contact__label">P:</span>+61 8 9400 5172</p>
      <p class="contact__row"><span class="contact__label">A:</span>address we could use PO Box 482,<br><span class="contact__indent">Perth WA 6000 Australia</span></p>
      <p class="contact__row"><span class="contact__label">E:</span>john.doe@verdantharbour.example</p>
      <p class="contact__row"><span class="contact__label">W:</span>www.verdantharbour.example</p>
    </div>
  </section>

  <section class="card card--front" aria-label="Card front">
    <div class="brand"><span class="brand__dot"></span><span class="brand__name">verdant harbour</span></div>
  </section>
</main>
</body>
</html>
```